Hello!
I am looking for a designer to create a business card for my business.
Logo attached. Preferred colors: blue gray. The business card should be elegant, professional, and similar to the business.

Final files should allow for editing: name, position, e-mail, telephone number, company website address.

Business card size: 90 x 50 mm

```html
<!DOCTYPE html>
<html lang="en">
<head>
<meta charset="utf-8">
<title>Business Card – Front and Back</title>
<link href="https://fonts.googleapis.com/css2?family=Lato:wght@400;700&display=swap" rel="stylesheet">
<style>
  :root {
    --stage: #5f5f5f;
    --paper: #ffffff;
    --blue-bright: #0fa0dc;
    --blue-mid: #1a86cc;
    --blue-deep: #1673bd;
    --ink: #3a3a3a;
    --ink-soft: #555555;
    --brand-ink: #222222;
  }
  * { margin: 0; padding: 0; box-sizing: border-box; }
  html, body {
    width: 1200px; height: 1200px; overflow: hidden;
    background: var(--stage);
    font-family: "Lato", Arial, sans-serif;
  }
  .canvas { position: relative; width: 1200px; height: 1200px; }

  .card {
    position: absolute; left: 148px; width: 903px; height: 541px;
    background: var(--paper); overflow: hidden;
  }
  .card--front { top: 40px; }
  .card--back { top: 619px; }

  .front-art { position: absolute; inset: 0; width: 100%; height: 100%; }

  .brand { position: absolute; display: flex; flex-direction: column; align-items: center; }
  .brand__mark { background: var(--blue-mid); }
  .brand__name { color: var(--brand-ink); font-weight: 400; letter-spacing: 0.04em; line-height: 1; }

  .card--front .brand { left: 352px; width: 200px; top: 196px; }
  .card--front .brand__mark { width: 62px; height: 62px; margin-bottom: 64px; }
  .card--front .brand__name { font-size: 29px; }

  .side-bar {
    position: absolute; left: 76px; top: 0; width: 56px; height: 100%;
    background: var(--blue-deep);
  }
  .identity { position: absolute; left: 152px; top: 100px; }
  .identity__name { font-size: 29px; font-weight: 700; color: var(--ink); line-height: 1.1; }
  .identity__role { font-size: 19px; color: var(--ink-soft); margin-top: 4px; letter-spacing: 0.02em; }

  .contacts { position: absolute; left: 0; top: 294px; list-style: none; }
  .contact {
    display: flex; align-items: center; height: 37.5px;
    font-size: 18px; color: var(--ink);
  }
  .contact__icon { width: 22px; height: 22px; margin-left: 93px; margin-right: 37px; fill: var(--paper); }

  .divider {
    position: absolute; left: 504px; top: 103px; width: 3px; height: 329px;
    background: var(--blue-deep);
  }

  .card--back .brand { left: 575px; width: 240px; top: 126px; }
  .card--back .brand__mark { width: 112px; height: 112px; margin-bottom: 96px; }
  .card--back .brand__name { font-size: 42px; }
</style>
</head>
<body>
<main class="canvas">

  <section class="card card--front" aria-label="Card front">
    <svg class="front-art" viewBox="0 0 677 406" preserveAspectRatio="none" aria-hidden="true">
      <defs>
        <linearGradient id="bandTop" x1="0" y1="0" x2="0" y2="1">
          <stop offset="0" stop-color="#0aa2de"/>
          <stop offset="1" stop-color="#1a84cb"/>
        </linearGradient>
        <linearGradient id="bandBottom" x1="0" y1="0" x2="0" y2="1">
          <stop offset="0" stop-color="#1675bf"/>
          <stop offset="1" stop-color="#0c9dda"/>
        </linearGradient>
      </defs>
      <polygon points="0,0 677,0 677,88 0,155" fill="url(#bandTop)"/>
      <polygon points="0,313 677,251 677,406 0,406" fill="url(#bandBottom)"/>
    </svg>
    <div class="brand">
      <div class="brand__mark"></div>
      <span class="brand__name">VERANO</span>
    </div>
  </section>

  <section class="card card--back" aria-label="Card back">
    <div class="side-bar"></div>

    <div class="identity">
      <p class="identity__name">John Due</p>
      <p class="identity__role">Web Designer</p>
    </div>

    <ul class="contacts">
      <li class="contact">
        <svg class="contact__icon" viewBox="0 0 24 24" aria-hidden="true"><path d="M12 2a7 7 0 0 0-7 7c0 5 7 13 7 13s7-8 7-13a7 7 0 0 0-7-7zm0 9.5A2.5 2.5 0 1 1 12 6.5a2.5 2.5 0 0 1 0 5z"/></svg>
        <span>Business Location,Country</span>
      </li>
      <li class="contact">
        <svg class="contact__icon" viewBox="0 0 24 24" aria-hidden="true"><path d="M6.6 10.8a15 15 0 0 0 6.6 6.6l2.2-2.2a1 1 0 0 1 1-.25 11.4 11.4 0 0 0 3.6.57 1 1 0 0 1 1 1V20a1 1 0 0 1-1 1A17 17 0 0 1 3 4a1 1 0 0 1 1-1h3.5a1 1 0 0 1 1 1c0 1.25.2 2.45.57 3.57a1 1 0 0 1-.25 1z"/></svg>
        <span>+123 456 789</span>
      </li>
      <li class="contact">
        <svg class="contact__icon" viewBox="0 0 24 24" aria-hidden="true"><path d="M3 6h18v2l-9 5-9-5z"/><path d="M3 10l9 5 9-5v8H3z"/></svg>
        <span>info@veranomail.com</span>
      </li>
      <li class="contact">
        <svg class="contact__icon" viewBox="0 0 24 24" aria-hidden="true"><path d="M12 2a10 10 0 1 0 0 20 10 10 0 0 0 0-20zm-1 17.9A8 8 0 0 1 4.2 10.2L9 15v1a2 2 0 0 0 2 2zm6.9-2.5A2 2 0 0 0 16 16h-1v-3a1 1 0 0 0-1-1H8v-2h2a1 1 0 0 0 1-1V7h2a2 2 0 0 0 2-2v-.4a8 8 0 0 1 2.9 12.8z"/></svg>
        <span>www.yoursite.com</span>
      </li>
    </ul>

    <div class="divider"></div>

    <div class="brand">
      <div class="brand__mark"></div>
      <span class="brand__name">VERANO</span>
    </div>
  </section>

</main>
</body>
</html>
```